PDN Letterhead

We need a letterhead design that will be able to be used on all marketing products (letterhead, mail chimp, envelops, business cards, etc.) We are a law firm specializing primarily in transportation law but offer a wide range of services to our clients. We would like the design to be modern, simple, and professional. Our colors are black and gold, however, we've incorporated dark gray and white on other marketing products such as our website.

```html
<!DOCTYPE html>
<html lang="en">
<head>
<meta charset="utf-8">
<title>PDN Letterhead</title>
<link href="https://fonts.googleapis.com/css2?family=Source+Sans+3:wght@400;600;700&family=Open+Sans:wght@700&display=swap" rel="stylesheet">
<style>
  :root {
    --backdrop: #b3b3b3;
    --paper: #ffffff;
    --gold: #b8996b;
    --ink: #1a1a1a;
    --body-text: #3d3d3d;
    --rule: #555555;
  }
  * { margin: 0; padding: 0; box-sizing: border-box; }
  html, body {
    width: 1012px; height: 1200px; overflow: hidden;
    background: var(--backdrop);
  }
  .letterhead {
    position: absolute; left: 118px; top: 89px;
    width: 788px; height: 1026px;
    background: var(--paper);
    font-family: "Source Sans 3", "Myriad Pro", sans-serif;
  }
  .brand {
    position: absolute; left: 65px; top: 92px;
    display: flex; align-items: center; gap: 10px;
  }
  .brand-square { width: 22px; height: 22px; background: var(--gold); }
  .brand-name {
    font-family: "Source Sans 3", sans-serif;
    font-weight: 600; font-size: 44px; letter-spacing: 3px;
    color: var(--ink); line-height: 1;
  }
  .letter-title {
    position: absolute; left: 65px; top: 219px;
    font-size: 18.5px; font-weight: 700; color: var(--gold);
  }
  .letter-body {
    position: absolute; left: 65px; top: 256px; width: 652px;
    font-size: 13.6px; line-height: 17.45px; color: var(--body-text);
    text-align: justify; hyphens: auto;
  }
  .letter-body p + p { margin-top: 17.45px; }
  .letter-body p.clipped { height: 104.7px; overflow: hidden; }
  .footer-rule {
    position: absolute; left: 65px; top: 927px; width: 659px;
    border-top: 1.6px solid var(--rule);
  }
  .contact {
    position: absolute; display: flex; align-items: center; gap: 11px;
    font-family: "Open Sans", sans-serif; font-weight: 700;
    font-size: 10.4px; line-height: 13.5px; color: var(--ink);
  }
  .contact svg { flex: none; }
  .contact-address { left: 66px; top: 955px; }
  .contact-phone { left: 278px; top: 955px; }
  .contact-web { left: 494px; top: 955px; }
</style>
</head>
<body>
<main class="letterhead">
  <div class="brand">
    <span class="brand-square"></span>
    <span class="brand-name">PDN</span>
  </div>

  <h1 class="letter-title">Lorem ipsum dolor sit amet</h1>

  <div class="letter-body" lang="la">
    <p>Lorem ipsum dolor sit amet, consectetur adipiscing elit, sed do eiusmod tempor incididunt ut labore et dolore magna aliqua. Ut enim ad minim veniam, quis nostrud exercitation ullamco laboris nisi ut aliquip ex ea commodo consequat. Duis aute irure dolor in reprehenderit in voluptate velit esse cillum dolore eu fugiat nulla pariatur. Excepteur sint occaecat cupidatat non proident, sunt in culpa qui officia deserunt mollit anim id est laborum Sed ut perspiciatis unde omnis iste natus error sit voluptatem accusantium doloremque laudantium, totam rem aperiam, eaque ipsa quae ab illo inventore veritatis et quasi architecto beatae vitae dicta sunt explicabo. Nemo enim ipsam voluptatem quia voluptas sit aspernatur aut odit aut fugit, sed quia consequuntur magni dolores eos qui ratione voluptatem sequi nesciunt. Neque porro quisquam est, qui dolorem ipsum quia dolor sit amet, consectetur, adipisci velit, sed quia non numquam eius modi tempora incidunt ut labore et dolore magnam aliquam quaerat voluptatem. Ut enim ad minima veniam, quis nostrum exercitationem ullam corporis suscipit laboriosam, nisi ut aliquid ex ea commodi consequatur? Quis autem vel eum iure reprehenderit qui in ea voluptate velit esse quam nihil molestiae consequatur, vel illum qui dolorem eum fugiat quo voluptas nulla pariatur?</p>
    <p>Lorem ipsum dolor sit amet, consectetur adipiscing elit, sed do eiusmod tempor incididunt ut labore et dolore magna aliqua. Ut enim ad minim veniam, quis nostrud exercitation ullamco laboris nisi ut aliquip ex ea commodo consequat. Duis aute irure dolor in reprehenderit in voluptate velit esse cillum dolore eu fugiat nulla pariatur. Excepteur sint occaecat cupidatat non proident, sunt in culpa qui officia deserunt mollit anim id est laborum Sed ut perspiciatis unde omnis iste natus error sit voluptatem accusantium doloremque laudantium, totam rem aperiam, eaque ipsa quae ab illo inventore veritatis et quasi architecto beatae vitae dicta sunt explicabo. Nemo enim ipsam voluptatem quia voluptas sit aspernatur aut odit aut fugit, sed quia consequuntur magni dolores eos qui ratione voluptatem sequi nesciunt. Neque porro quisquam est, qui dolorem ipsum quia dolor sit amet, consectetur, adipisci velit, sed quia non numquam eius modi tempora incidunt ut labore et dolore magnam aliquam quaerat voluptatem. Ut enim ad minima veniam, quis nostrum exercitationem ullam corporis suscipit laboriosam, nisi ut aliquid ex ea commodi consequatur? Quis autem vel eum iure reprehenderit qui in ea voluptate velit esse quam nihil molestiae consequatur, vel illum qui dolorem eum fugiat quo voluptas nulla pariatur?</p>
    <p class="clipped">Lorem ipsum dolor sit amet, consectetur adipiscing elit, sed do eiusmod tempor incididunt ut labore et dolore magna aliqua. Ut enim ad minim veniam, quis nostrud exercitation ullamco laboris nisi ut aliquip ex ea commodo consequat. Duis aute irure dolor in reprehenderit in voluptate velit esse cillum dolore eu fugiat nulla pariatur. Excepteur sint occaecat cupidatat non proident, sunt in culpa qui officia deserunt mollit anim id est laborum Sed ut perspiciatis unde omnis iste natus error sit voluptatem accusantium doloremque laudantium, totam rem aperiam, eaque ipsa quae ab illo inventore veritatis et quasi architecto beatae vitae dicta sunt explicabo.</p>
  </div>

  <div class="footer-rule"></div>

  <div class="contact contact-address">
    <svg width="32" height="32" viewBox="0 0 32 32" aria-hidden="true">
      <circle cx="16" cy="16" r="16" fill="var(--gold)"/>
      <path d="M16 8.5a5 5 0 0 0-5 5c0 3.8 5 9.5 5 9.5s5-5.7 5-9.5a5 5 0 0 0-5-5z" fill="#fff"/>
      <circle cx="16" cy="13.5" r="1.9" fill="var(--gold)"/>
    </svg>
    <address style="font-style:normal">820 Harbor Point<br>Avenue, Suite 210<br>Coral Bay, FL 33000</address>
  </div>

  <div class="contact contact-phone">
    <svg width="32" height="32" viewBox="0 0 32 32" aria-hidden="true">
      <circle cx="16" cy="16" r="16" fill="var(--gold)"/>
      <path d="M11.2 9.2c.5-.4 1.2-.3 1.5.2l1.6 2.4c.3.5.2 1.1-.2 1.4l-1 .8c.7 1.7 2 3 3.7 3.8l.8-1c.3-.4 1-.5 1.4-.2l2.4 1.6c.5.3.6 1 .2 1.5l-1 1.2c-.5.6-1.3.8-2 .6-4-1.3-7-4.3-8.3-8.3-.2-.7 0-1.5.6-2z" fill="#fff"/>
    </svg>
    <span>TELEPHONE: 555.014.2290</span>
  </div>

  <div class="contact contact-web">
    <svg width="32" height="32" viewBox="0 0 32 32" aria-hidden="true">
      <circle cx="16" cy="16" r="16" fill="var(--gold)"/>
      <g fill="none" stroke="#fff" stroke-width="1.2">
        <circle cx="16" cy="16" r="6.5"/>
        <ellipse cx="16" cy="16" rx="2.8" ry="6.5"/>
        <path d="M9.5 16h13M10.5 12.8h11M10.5 19.2h11"/>
      </g>
    </svg>
    <span>www.pdnlegal.com<br>admin@pdnlegal.com</span>
  </div>
</main>
</body>
</html>
```